84M business card

I need a business card for a life sciences consulting firm I started. The company name is 84M and the logo is attached. I am looking for something edgey and current but different from the blah standard business card.

Industry/Entity Type

Business

Requirements
Nice to have
• Both sides

```html
<!DOCTYPE html>
<html lang="en">
<head>
<meta charset="utf-8">
<title>84M LLC — Business Card</title>
<link rel="stylesheet" href="https://fonts.googleapis.com/css2?family=Open+Sans:wght@400;600&display=swap">
<style>
  :root {
    --stage: #2b2b2b;
    --navy: #1b3f8f;
    --navy-deep: #10307a;
    --blue-light: #1f5cb0;
    --orange: #e8641b;
    --ink: #1a1a1a;
    --paper: #f7f7f7;
    --white: #ffffff;
    --muted: #9fb4dc;
  }
  * { margin: 0; padding: 0; box-sizing: border-box; }
  html, body {
    width: 1200px; height: 900px; overflow: hidden;
    background: var(--stage);
    font-family: "Open Sans", Arial, sans-serif;
  }
  .stage {
    position: relative; width: 1200px; height: 900px;
  }
  .card {
    position: absolute; left: 337px; width: 525px; height: 300px;
    box-shadow: 0 10px 30px rgba(0,0,0,.5);
  }
  .card-front {
    top: 110px;
    background: radial-gradient(ellipse at 55% 50%, var(--blue-light) 0%, var(--navy) 55%, var(--navy-deep) 100%);
  }
  .card-back { top: 470px; background: var(--paper); }

  .brand {
    position: absolute; left: 0; right: 0; top: 108px;
    display: flex; align-items: center; justify-content: center; gap: 20px;
  }
  .brand-mark {
    width: 78px; height: 78px; border-radius: 50%; background: var(--white);
  }
  .brand-text { color: var(--white); }
  .brand-name {
    font-size: 58px; font-weight: 600; line-height: 1; letter-spacing: 2px;
  }
  .brand-name .suffix { font-size: 18px; letter-spacing: 1px; margin-left: 4px; }
  .brand-tagline {
    font-size: 11px; font-weight: 400; margin-top: 6px; letter-spacing: .5px; color: var(--muted);
  }

  .person { position: absolute; left: 40px; top: 150px; }
  .person-name { font-size: 26px; font-weight: 400; color: var(--ink); line-height: 1.05; }
  .person-role { font-size: 19px; font-weight: 400; color: var(--orange); line-height: 1.1; }
  .contact { list-style: none; margin-top: 22px; }
  .contact li {
    display: flex; align-items: center; gap: 10px;
    font-size: 13px; color: var(--ink); margin-bottom: 7px;
  }
  .contact svg { width: 16px; height: 16px; }

  .back-mark {
    position: absolute; right: 48px; top: 58px;
    display: flex; align-items: center; gap: 14px;
  }
  .back-mark .dot {
    width: 120px; height: 120px; border-radius: 50%; background: var(--navy);
  }
  .back-mark .name {
    font-size: 40px; font-weight: 600; color: var(--navy);
  }
</style>
</head>
<body>
<main class="stage">
  <section class="card card-front" aria-label="Business card front">
    <div class="brand">
      <span class="brand-mark"></span>
      <div class="brand-text">
        <div class="brand-name">84M<span class="suffix">LLC</span></div>
        <div class="brand-tagline">regulatory consulting and contract services</div>
      </div>
    </div>
  </section>

  <section class="card card-back" aria-label="Business card back">
    <div class="person">
      <div class="person-name">YOUR NAME</div>
      <div class="person-role">Company Position</div>
      <ul class="contact">
        <li>
          <svg viewBox="0 0 16 16" aria-hidden="true"><circle cx="8" cy="8" r="7" fill="none" stroke="#e8641b" stroke-width="1.5"/><path d="M5.5 4.5l1.5 1.5-1 1c.6 1.2 1.5 2.1 2.7 2.7l1-1 1.5 1.5-1 1.3c-2.6-.4-4.6-2.4-5-5z" fill="#e8641b"/></svg>
          000 000 000
        </li>
        <li>
          <svg viewBox="0 0 16 16" aria-hidden="true"><circle cx="8" cy="8" r="7" fill="none" stroke="#e8641b" stroke-width="1.5"/><rect x="4.5" y="5.5" width="7" height="5" fill="#e8641b"/><path d="M4.5 5.5l3.5 3 3.5-3" fill="none" stroke="#f7f7f7" stroke-width="0.8"/></svg>
          youremail@domain.com
        </li>
      </ul>
    </div>
    <div class="back-mark">
      <span class="dot"></span>
      <span class="name">84M</span>
    </div>
  </section>
</main>
</body>
</html>
```